Business Card and Logo Color Scheme Design Contest

We are starting a new company called Lonestar Precision Surveying and already have a logo however, the colors for the logo itself are not final and COULD be changed. I'm hoping to move AWAYfrom the gold color in the card and the logo as it seems a bit outdated. What we need help with is to find what our business color scheme will be, and then incorporate those colors into both the logo and the business card design itself. We also want to make sure we are known as "LPS" so in the future we can just refer to ourselves as "LPS" and not Lonestar Precision Surveying. That being said, I would like to make a slight change to the logo to somehow include the letters "LPS." The logo used in the front of the card design MUST ALSO include the words "Firm No. 64307" within the logo. My vision is for the front of the card to have the information shown in the attached image. For the back of the card, I'm hoping to have something very simple. I'm envisioning a solid color with either the website (www.surveyplainsco.com) and a simplified version of the logo. I've attached an example but I'm looking for a complete redesign. I'm looking for a slick, modern and simple design.

Industry/Entity Type

Civil Engineer

Contact Information for Business Card

Logo
Firm No. 64307
Marcus Holloway, PE
Chief Operating Officer
Email:mholloway@surveyplainsco.com
Ph: 936.482.3095 | D: 936.482.3067 | M:210.347.6152
4718 W. Bramwell, Conroe, Texas 77318
www.surveyplainsco.com

Requirements
Must have
• Logo
Contact Info
Nice to have
• "LPS" Incorporated in the design
Should not have
• The current color scheme

```html
<!DOCTYPE html>
<html lang="en">
<head>
<meta charset="utf-8">
<title>Lonestar Precision Surveying – Business Card</title>
<link rel="stylesheet" href="https://fonts.googleapis.com/css2?family=Montserrat:wght@400;500;600;700&display=swap">
<style>
  :root {
    --backdrop: #e7e9ec;
    --card-white: #ffffff;
    --navy: #17324f;
    --navy-mid: #1d4a6b;
    --teal: #1b8c8a;
    --teal-light: #2fb3a6;
    --text-grey: #5f6670;
    --rule: #8cc9c3;
  }
  * { box-sizing: border-box; margin: 0; padding: 0; }
  html, body { width: 1200px; height: 1091px; overflow: hidden; }
  body {
    background: var(--backdrop);
    font-family: "Montserrat", sans-serif;
    position: relative;
  }
  .card {
    position: absolute;
    border-radius: 4px;
    box-shadow: 0 18px 40px rgba(0,0,0,.18), 0 3px 8px rgba(0,0,0,.12);
    overflow: hidden;
  }

  /* Front card – portrait */
  .card-front {
    left: 70px; top: 223px;
    width: 369px; height: 645px;
    background: var(--card-white);
    border-right: 6px solid var(--teal);
    text-align: center;
    color: var(--text-grey);
  }
  .brand {
    margin: 70px auto 0;
    width: 290px;
    display: flex;
    align-items: center;
    gap: 14px;
    text-align: left;
  }
  .brand-dot {
    flex: none;
    width: 44px; height: 44px;
    border-radius: 50%;
    background: var(--teal);
  }
  .brand-name {
    font-weight: 700;
    font-size: 19px;
    line-height: 1.2;
    color: var(--navy);
    text-transform: uppercase;
    letter-spacing: .5px;
  }
  .brand-firm {
    margin-top: 8px;
    font-size: 11px;
    letter-spacing: 1px;
    color: var(--navy);
    font-weight: 700;
    text-transform: uppercase;
  }
  .person { margin-top: 95px; }
  .person-name {
    font-size: 22px;
    font-weight: 600;
    color: var(--teal);
  }
  .person-title {
    margin-top: 4px;
    font-size: 16px;
    font-weight: 400;
  }
  .divider {
    display: flex;
    align-items: center;
    justify-content: center;
    gap: 10px;
    margin: 26px auto 18px;
  }
  .divider .rule { width: 44px; height: 1px; background: var(--rule); }
  .divider svg { display: block; }
  .contact-line {
    font-size: 14px;
    line-height: 1.75;
    letter-spacing: .2px;
  }

  /* Back card – landscape */
  .card-back {
    left: 495px; top: 361px;
    width: 645px; height: 369px;
    background: linear-gradient(135deg, var(--navy) 0%, var(--navy-mid) 45%, var(--teal) 100%);
    color: #fff;
  }
  .back-mark {
    position: absolute;
    left: 0; right: 0; top: 118px;
    text-align: center;
  }
  .back-initials {
    font-size: 84px;
    font-weight: 700;
    letter-spacing: 6px;
    line-height: 1;
  }
  .back-firm {
    margin-top: 10px;
    font-size: 15px;
    font-weight: 500;
    letter-spacing: 2px;
  }
  .back-web {
    position: absolute;
    left: 40px; bottom: 34px;
    font-size: 14px;
    letter-spacing: .5px;
  }
</style>
</head>
<body>

  <section class="card card-front" aria-label="Business card front">
    <div class="brand">
      <span class="brand-dot"></span>
      <div>
        <div class="brand-name">Lonestar Precision Surveying, LLC</div>
        <div class="brand-firm">Firm No. 64307</div>
      </div>
    </div>

    <div class="person">
      <div class="person-name">Marcus Holloway, PE</div>
      <div class="person-title">Chief Operating Officer</div>
    </div>

    <div class="divider">
      <span class="rule"></span>
      <svg width="96" height="14" viewBox="0 0 96 14" fill="var(--teal)" aria-hidden="true">
        <rect x="0" y="4" width="12" height="8" rx="2"/>
        <rect x="3" y="1" width="6" height="3" rx="1"/>
        <path d="M27 2c1 0 2 2 2 3s-1 1-1 2 2 3 3 3 1-1 2-1 3 1 3 2-1 2-2 2C29 13 25 8 25 4c0-1 1-2 2-2z"/>
        <rect x="49" y="1" width="7" height="12" rx="1.5" fill="none" stroke="var(--teal)" stroke-width="1.6"/>
        <rect x="67" y="3" width="12" height="9" rx="1.5"/>
        <path d="M67 4l6 4 6-4" fill="none" stroke="#fff" stroke-width="1.2"/>
        <circle cx="90" cy="7.5" r="5.5"/>
        <path d="M84.5 7.5h11M90 2c-2 3-2 8 0 11M90 2c2 3 2 8 0 11" fill="none" stroke="#fff" stroke-width="1"/>
      </svg>
      <span class="rule"></span>
    </div>

    <p class="contact-line">936.482.3095 | 936.482.3067 | 210.347.6152</p>
    <p class="contact-line">mholloway@surveyplainsco.com</p>
    <p class="contact-line">surveyplainsco.com</p>

    <div class="divider">
      <span class="rule"></span>
      <svg width="12" height="16" viewBox="0 0 12 16" aria-hidden="true">
        <path d="M6 0C2.7 0 0 2.6 0 5.9 0 10.3 6 16 6 16s6-5.7 6-10.1C12 2.6 9.3 0 6 0z" fill="var(--teal)"/>
        <circle cx="6" cy="6" r="2.2" fill="#fff"/>
      </svg>
      <span class="rule"></span>
    </div>

    <p class="contact-line">4718 W. Bramwell, Conroe, Texas 77318</p>
  </section>

  <section class="card card-back" aria-label="Business card back">
    <div class="back-mark">
      <div class="back-initials">LPS</div>
      <div class="back-firm">Firm No. 64307</div>
    </div>
    <div class="back-web">www.surveyplainsco.com</div>
  </section>

</body>
</html>
```